Federal Government Proposal Development Consulting company needs a website designed and coded

I am looking for someone to design (using an existing logo, color palette, and text fonts) and code a wordpress-based website for a Proposal Development consulting company. I have full copy for all site pages and suggestions for images/ graphics and a few example design templates to go from.

One note, from a color perspective - I included a mockup of a business card to highlight a color scheme that I tend to like - if you look at the back of the business card, the blend of the grey, blue, with the neon green highlight as a separator really seems to pop. Just a thought as you are designing the page.

I would like to see 2-3 potential design layouts, and I will select one to move forward with. Then, I would like the site to be coded for WordPress (I can provide a login to my wordpress site). I would like 1 opportunity to review the coded site and make any final tweaks.

```html
<!DOCTYPE html>
<html lang="en">
<head>
<meta charset="utf-8">
<title>The Clear Quill Consulting</title>
<link href="https://fonts.googleapis.com/css2?family=Jost:wght@400;500;600&family=Open+Sans:wght@400;600;700&display=swap" rel="stylesheet">
<style>
:root{
  --blue:#0b2fc0;
  --blue-deep:#06176e;
  --teal:#2fe6c8;
  --ink:#1f1f24;
  --muted:#55565e;
  --navy:#070d2b;
  --grey-bg:#f1f1f4;
  --white:#ffffff;
}
*{box-sizing:border-box;margin:0;padding:0}
html,body{width:1200px;height:4874px;overflow:hidden}
body{position:relative;font-family:"Open Sans",sans-serif;color:var(--ink);background:var(--white)}
.abs{position:absolute}
h1,h2,h3,.nav a,.btn{font-family:"Jost",sans-serif}
.btn{position:absolute;display:flex;align-items:center;justify-content:center;background:linear-gradient(90deg,var(--blue-deep),var(--blue));color:#fff;font-size:12px;font-weight:600;letter-spacing:.3px;border-radius:4px;text-transform:uppercase}
.section-title{position:absolute;left:0;width:1200px;text-align:center;font-size:34px;font-weight:500;color:var(--ink)}

/* header */
.site-header{position:absolute;left:0;top:0;width:1200px;height:93px;background:#fff;z-index:5;box-shadow:0 1px 4px rgba(0,0,0,.08)}
.brand-box{position:absolute;left:97px;top:0;width:249px;height:117px;background:#fff;border-radius:0 0 8px 8px;box-shadow:0 3px 8px rgba(0,0,0,.12);display:flex;align-items:center;justify-content:center;gap:10px;z-index:6}
.brand-name{font-family:"Jost",sans-serif;font-size:25px;font-weight:500;color:#3a3d52}
.brand-dot{width:16px;height:16px;border-radius:50%;background:var(--blue)}
.nav a{position:absolute;top:38px;font-size:16px;color:#222;text-decoration:none}
.search{position:absolute;left:1058px;top:37px}

/* hero */
.hero{position:absolute;left:0;top:93px;width:1200px;height:655px;background:linear-gradient(100deg,#2b2a6b 0%,#4a3a7e 35%,#7e6d9a 60%,#3a5b96 85%,#1f3f88 100%)}
.hero h1{position:absolute;left:110px;top:152px;font-size:46px;font-weight:500;color:#fff}
.hero p{position:absolute;left:110px;top:228px;font-family:"Jost",sans-serif;font-size:31px;line-height:47px;color:#fff;font-weight:400}

/* what we do */
.intro{position:absolute;left:127px;top:840px;width:946px;text-align:center;font-size:12.6px;line-height:22px;color:#333}
.service-card{position:absolute;top:1037px;width:308px;height:341px;background:#fff;box-shadow:0 2px 10px rgba(0,0,0,.12);border-bottom:5px solid var(--teal)}
.service-card .icon{position:absolute;left:28px;top:-20px;width:96px;height:96px;border-radius:50%;background:#fff;box-shadow:0 1px 6px rgba(0,0,0,.12);display:flex;align-items:center;justify-content:center}
.service-card h3{position:absolute;left:26px;top:93px;font-size:18px;font-weight:500}
.service-card ul{position:absolute;left:26px;top:136px;width:266px;list-style:none}
.service-card li{position:relative;padding-left:24px;font-size:9.6px;line-height:16px;color:#666;text-align:justify;margin-bottom:10px}
.service-card li::before{content:"";position:absolute;left:0;top:3px;width:10px;height:10px;border-radius:50%;background:#1c1f3a}

/* who we are */
.who{position:absolute;left:0;top:1467px;width:1200px;height:591px;background:linear-gradient(180deg,#dcdde6,#e7e7ee 60%,#eaeaf0)}
.who p{position:absolute;left:161px;top:225px;width:877px;text-align:center;font-size:14.6px;line-height:25.7px;color:#333}

/* services */
.svc{position:absolute;display:flex;align-items:flex-end;justify-content:center;padding-bottom:28px;color:#fff;font-family:"Jost",sans-serif;font-weight:600;font-size:16px}
.arrow{position:absolute;width:40px;height:40px;border-radius:50%;border:2px solid}

/* expertise */
.expertise{position:absolute;left:0;top:2754px;width:1200px;height:602px;background:var(--grey-bg)}
.exp-list{position:absolute;left:110px;top:140px;list-style:none}
.exp-list li{display:flex;align-items:center;gap:12px;height:37.7px;font-size:16px;color:#333}

/* contact */
.contact{position:absolute;left:0;top:3356px;width:1200px;height:591px;background:linear-gradient(120deg,#0c1649,#1b2a6a 45%,#0a1240)}
.field{position:absolute;background:#fff;border-radius:2px;font-size:14px;color:#666;padding:14px 20px}
.field svg{position:absolute;right:20px;top:16px}

/* testimonials */
.t-card{position:absolute;top:4085px;width:304px;height:303px;background:#fff;box-shadow:0 2px 10px rgba(0,0,0,.12);text-align:center}
.t-card .avatar{position:absolute;left:104px;top:31px;width:96px;height:96px;border-radius:50%}
.t-card .quote{position:absolute;left:34px;top:138px;font-family:"Jost",sans-serif;font-size:52px;line-height:1;color:#c4d3f5}
.t-card h3{position:absolute;left:0;width:100%;top:142px;font-size:18px;font-weight:500}
.t-card p{position:absolute;left:32px;width:240px;top:182px;font-size:12px;line-height:21px;color:#666}
.t-card .stars{position:absolute;left:0;width:100%;top:260px;color:#f5b400;font-size:15px;letter-spacing:1px}

/* footer */
.footer{position:absolute;left:0;top:4470px;width:1200px;height:404px;background:var(--navy)}
.footer h4{position:absolute;top:185px;font-size:14px;font-weight:600;color:#fff;letter-spacing:.3px}
.footer .item{position:absolute;font-size:14px;color:#fff;line-height:24px}
.footer .links a{display:block;color:#fff;text-decoration:none;font-size:15px;line-height:25.8px}
</style>
</head>
<body>

<header class="site-header">
  <div class="brand-box"><span class="brand-name">The Clear Quill</span><span class="brand-dot"></span></div>
  <nav class="nav">
    <a style="left:496px">Home</a>
    <a style="left:579px">Work with Us</a>
    <a style="left:714px">Work for Us</a>
    <a style="left:840px">About Us</a>
    <a style="left:946px">Contact</a>
  </nav>
  <svg class="search" width="22" height="22" viewBox="0 0 22 22"><circle cx="9" cy="9" r="7" fill="none" stroke="#2fd9bd" stroke-width="3"/><line x1="14" y1="14" x2="20" y2="20" stroke="#2fd9bd" stroke-width="3" stroke-linecap="round"/></svg>
</header>

<section class="hero" role="img" aria-label="Engineer in hard hat and safety glasses working on a laptop">
  <h1>Generate Success</h1>
  <p>Fuel Innovation in Proposal<br>Excellence with The Clear Quill!<br>Click here to explore our services.</p>
  <a class="btn" style="left:110px;top:409px;width:138px;height:49px">Get Started</a>
</section>
<svg class="abs" style="left:0;top:640px" width="1200" height="110" viewBox="0 0 1200 110">
  <polygon points="0,89 290,19 1200,100 1200,110 0,110" fill="var(--blue)"/>
  <polygon points="0,104 290,34 1200,108 1200,110 0,110" fill="#fff"/>
</svg>

<h2 class="section-title" style="top:772px">What We Do</h2>
<p class="intro">The Clear Quill, specializes in advancing an organization through a comprehensive suite of services designed to modernize the proposal development process. From innovative Capture Management strategies that pinpoint lucrative opportunities, meticulous Proposal Development services that transform concepts into effective narratives, and cutting-edge Generative AI techniques that create domain-aware content accelerating proposal draft development, we are your dedicated partner in securing success. With a unique fusion of technical expertise and exceptional writing capabilities, we surpass industry standards and set new benchmarks for excellence. Discover a dynamic approach to proposal consulting that goes beyond conventional boundaries—choose The Clear Quill for solutions that Enhance the quality of your work, Elevate your corporate advantage, and Expand your industry presence.</p>

<div class="service-card" style="left:112px">
  <div class="icon"><svg width="48" height="48" viewBox="0 0 48 48" fill="none" stroke="#1a2a8a" stroke-width="2"><rect x="8" y="6" width="26" height="34" rx="2"/><line x1="14" y1="14" x2="28" y2="14"/><line x1="14" y1="21" x2="28" y2="21"/><rect x="26" y="26" width="16" height="16" rx="2"/><polyline points="30,35 33,38 38,31"/></svg></div>
  <h3>Capture Management</h3>
  <ul>
    <li>Elevate your business development strategy with our Capture Management services. From opportunity identification to strategic planning, our experts will guide you through a meticulous process, ensuring the pursuit of the right contracts to position your organization for success.</li>
    <li>Trust us to analyze the market, mitigate risks, and develop strategies that maximize the ability to secure lucrative opportunities.</li>
  </ul>
</div>
<div class="service-card" style="left:445px">
  <div class="icon"><svg width="48" height="48" viewBox="0 0 48 48" fill="none" stroke="#1a2a8a" stroke-width="2"><rect x="12" y="6" width="22" height="28" rx="2"/><line x1="17" y1="13" x2="29" y2="13"/><line x1="17" y1="19" x2="29" y2="19"/><path d="M6 34 q8 -6 16 0 l10 6 q4 2 8 -2"/><line x1="36" y1="10" x2="42" y2="4"/></svg></div>
  <h3>Proposal Development</h3>
  <ul>
    <li>Transform your vision into winning proposals with our Proposal Development services. We specialize in persuasive narratives, clear technical solutions, and strategic pricing models. From meticulous compliance reviews to captivating executive summaries, we ensure every aspect of a proposal is polished and aligned with your objectives.</li>
    <li>Turn your ideas into persuasive documents that leave a lasting impression on clients to set you apart from the competition.</li>
  </ul>
</div>
<div class="service-card" style="left:776px">
  <div class="icon"><svg width="50" height="50" viewBox="0 0 50 50" fill="none" stroke="#1a2a8a" stroke-width="2"><circle cx="25" cy="25" r="11"/><text x="25" y="29" text-anchor="middle" font-family="Jost,sans-serif" font-size="10" fill="#1a2a8a" stroke="none" font-weight="600">AI</text><line x1="25" y1="4" x2="25" y2="12"/><line x1="25" y1="38" x2="25" y2="46"/><line x1="4" y1="25" x2="12" y2="25"/><line x1="38" y1="25" x2="46" y2="25"/><line x1="10" y1="10" x2="16" y2="16"/><line x1="40" y1="10" x2="34" y2="16"/><line x1="10" y1="40" x2="16" y2="34"/><line x1="40" y1="40" x2="34" y2="34"/></svg></div>
  <h3>Generative AI</h3>
  <ul>
    <li>Revolutionize your proposal writing process with our domain-aware Generative AI services. Using customer-installed tools, we leverage domain-aware artificial intelligence to generate innovative and tailored proposal content. This not only accelerates the proposal development timeline but also ensures content that is both dynamic and targeted.</li>
    <li>Stay ahead of the curve with proposals that not only meet industry standards but exceed expectations, thanks</li>
  </ul>
</div>

<section class="who" role="img" aria-label="Faded photo of a team reviewing documents at a desk">
  <h2 class="section-title" style="top:145px">Who We Are</h2>
  <p>Lorem ipsum dolor sit amet, consectetur adipiscing elit, sed do eiusmod tempor incididunt ut labore et dolore magna aliqua. Ut enim ad minim veniam, quis nostrud exercitation ullamco laboris nisi ut aliquip ex ea commodo consequat. Duis aute irure dolor in reprehenderit in voluptate velit esse cillum dolore eu fugiat nulla pariatur. Excepteur sint occaecat cupidatat non proident, sunt in culpa qui officia deserunt mollit anim id est laborum.Sed ut perspiciatis unde omnis iste natus error sit voluptatem accusantium doloremque laudantium, totam rem aperiam, eaque ipsa quae ab illo inventore veritatis et quasi architecto beatae vitae dicta sunt explicabo. Nemo enim ipsam voluptatem quia voluptas sit aspernatur aut odit aut fugit, sed quia consequuntur magni dolores eos qui ratione voluptatem sequi nesciunt.</p>
  <a class="btn" style="left:532px;top:439px;width:136px;height:50px">Learn More</a>
</section>
<svg class="abs" style="left:0;top:1460px" width="1200" height="100" viewBox="0 0 1200 100">
  <polygon points="0,0 1200,0 1200,9 908,92 0,11" fill="#fff"/>
  <polygon points="0,7 908,88 1200,5 1200,15 908,98 0,17" fill="var(--blue)"/>
</svg>

<h2 class="section-title" style="top:2136px">Our Services</h2>
<div class="svc" style="left:112px;top:2262px;width:214px;height:360px;background:linear-gradient(180deg,#0f2a52,#1d3c6e 55%,#0a1630)" role="img" aria-label="Glowing digital network in a hand">Generative AI</div>
<div class="svc" style="left:333px;top:2224px;width:290px;height:436px;background:linear-gradient(180deg,#3e4e5c 0%,#56646c 50%,#3ad8bc 78%,#2fe6c8 100%);font-size:20px;padding-bottom:52px" role="img" aria-label="Two professionals discussing charts on a screen">Technical Solutioning</div>
<div class="svc" style="left:630px;top:2262px;width:212px;height:360px;background:linear-gradient(180deg,#28486a,#3b5370 50%,#14202e)" role="img" aria-label="Hand signing a document with a pen">Executive Summaries</div>
<div class="svc" style="left:850px;top:2262px;width:238px;height:360px;background:linear-gradient(180deg,#b7bcbf,#8c918f 55%,#2e3234)" role="img" aria-label="Thoughtful woman at a desk">Proposal Management</div>
<div class="arrow" style="left:24px;top:2424px;border-color:#777"><svg width="36" height="36" viewBox="0 0 36 36"><polyline points="21,11 14,18 21,25" fill="none" stroke="#777" stroke-width="2"/></svg></div>
<div class="arrow" style="left:1123px;top:2424px;border-color:#1ed8b7"><svg width="36" height="36" viewBox="0 0 36 36"><polyline points="15,11 22,18 15,25" fill="none" stroke="#1ed8b7" stroke-width="2"/></svg></div>

<section class="expertise">
  <h2 class="abs" style="left:110px;top:60px;font-size:35px;font-weight:500">Subject Matter Expertise</h2>
  <ul class="exp-list">
    <li><svg width="16" height="16" viewBox="0 0 16 16"><circle cx="8" cy="8" r="6.5" fill="none" stroke="#2a44c0" stroke-width="1.5"/><polyline points="5,8 7.3,10.2 11.5,5.5" fill="none" stroke="#2a44c0" stroke-width="1.5"/></svg>Generative AI</li>
    <li><svg width="16" height="16" viewBox="0 0 16 16"><circle cx="8" cy="8" r="6.5" fill="none" stroke="#2a44c0" stroke-width="1.5"/><polyline points="5,8 7.3,10.2 11.5,5.5" fill="none" stroke="#2a44c0" stroke-width="1.5"/></svg>Hardware Engineering</li>
    <li><svg width="16" height="16" viewBox="0 0 16 16"><circle cx="8" cy="8" r="6.5" fill="none" stroke="#2a44c0" stroke-width="1.5"/><polyline points="5,8 7.3,10.2 11.5,5.5" fill="none" stroke="#2a44c0" stroke-width="1.5"/></svg>Systems Engineering</li>
    <li><svg width="16" height="16" viewBox="0 0 16 16"><circle cx="8" cy="8" r="6.5" fill="none" stroke="#2a44c0" stroke-width="1.5"/><polyline points="5,8 7.3,10.2 11.5,5.5" fill="none" stroke="#2a44c0" stroke-width="1.5"/></svg>High-Performance Computing (HPC)</li>
    <li><svg width="16" height="16" viewBox="0 0 16 16"><circle cx="8" cy="8" r="6.5" fill="none" stroke="#2a44c0" stroke-width="1.5"/><polyline points="5,8 7.3,10.2 11.5,5.5" fill="none" stroke="#2a44c0" stroke-width="1.5"/></svg>Secure Supply Chain (ISO 28000 &amp; ISO 20243-1)</li>
    <li><svg width="16" height="16" viewBox="0 0 16 16"><circle cx="8" cy="8" r="6.5" fill="none" stroke="#2a44c0" stroke-width="1.5"/><polyline points="5,8 7.3,10.2 11.5,5.5" fill="none" stroke="#2a44c0" stroke-width="1.5"/></svg>Logistics</li>
    <li><svg width="16" height="16" viewBox="0 0 16 16"><circle cx="8" cy="8" r="6.5" fill="none" stroke="#2a44c0" stroke-width="1.5"/><polyline points="5,8 7.3,10.2 11.5,5.5" fill="none" stroke="#2a44c0" stroke-width="1.5"/></svg>Warehousing</li>
    <li><svg width="16" height="16" viewBox="0 0 16 16"><circle cx="8" cy="8" r="6.5" fill="none" stroke="#2a44c0" stroke-width="1.5"/><polyline points="5,8 7.3,10.2 11.5,5.5" fill="none" stroke="#2a44c0" stroke-width="1.5"/></svg>Information Technology Support</li>
    <li><svg width="16" height="16" viewBox="0 0 16 16"><circle cx="8" cy="8" r="6.5" fill="none" stroke="#2a44c0" stroke-width="1.5"/><polyline points="5,8 7.3,10.2 11.5,5.5" fill="none" stroke="#2a44c0" stroke-width="1.5"/></svg>Cybersecurity</li>
  </ul>
  <a class="btn" style="left:110px;top:489px;width:138px;height:49px">Learn More</a>
  <div class="abs" style="left:761px;top:74px;width:290px;height:343px;border:4px solid var(--teal);border-radius:14px"></div>
  <div class="abs" style="left:602px;top:103px;width:420px;height:414px;border-radius:18px;background:radial-gradient(circle at 65% 55%,#c43a4a 0%,#5a3a8a 30%,#1d4fae 60%,#0a2a70 100%)" role="img" aria-label="Android figure touching a futuristic digital interface"></div>
</section>

<section class="contact" role="img" aria-label="Dark blue overlay on a photo of a business meeting">
  <h2 class="section-title" style="top:70px;color:#fff">Contact Us</h2>
  <div class="field" style="left:134px;top:161px;width:462px;height:46px">First Name<svg width="12" height="12" viewBox="0 0 12 12"><circle cx="6" cy="3.5" r="3" fill="#555"/><path d="M0 12 q6 -9 12 0z" fill="#555"/></svg></div>
  <div class="field" style="left:606px;top:161px;width:460px;height:46px">Last Name<svg width="12" height="12" viewBox="0 0 12 12"><circle cx="6" cy="3.5" r="3" fill="#555"/><path d="M0 12 q6 -9 12 0z" fill="#555"/></svg></div>
  <div class="field" style="left:134px;top:222px;width:462px;height:49px">Email Address<svg width="14" height="11" viewBox="0 0 14 11"><rect width="14" height="11" fill="#555"/><polyline points="0,0 7,6 14,0" fill="none" stroke="#fff" stroke-width="1.2"/></svg></div>
  <div class="field" style="left:606px;top:222px;width:460px;height:49px">Phone No<svg width="12" height="12" viewBox="0 0 12 12"><path d="M2 0 l3 3 -1.5 2 q1.5 3 3.5 3.5 l2 -1.5 3 3 -2 2 q-7 0 -10 -10z" fill="#555"/></svg></div>
  <div class="field" style="left:134px;top:282px;width:932px;height:99px">Message<svg width="13" height="11" viewBox="0 0 13 11"><ellipse cx="6.5" cy="5" rx="6" ry="4.3" fill="none" stroke="#555" stroke-width="1.3"/></svg></div>
  <a class="btn" style="left:532px;top:415px;width:136px;height:49px">Submit Now</a>
</section>
<svg class="abs" style="left:0;top:3880px" width="1200" height="70" viewBox="0 0 1200 70">
  <polygon points="0,67 1200,5 1200,17 0,70" fill="var(--blue)"/>
  <polygon points="1200,17 1200,70 0,70" fill="#fff"/>
</svg>

<h2 class="section-title" style="top:3998px">Testimonials</h2>
<div class="t-card" style="left:112px"><div class="avatar" style="background:linear-gradient(180deg,#f2a46a,#e0753a)" role="img" aria-label="Portrait of a smiling man"></div><span class="quote">“</span><h3>Jordan Reyes</h3><p>Lorem ipsum dolor sit amet, consectetur adipiscing elit, sed do eiusmod tempor incididunt ut labore et dolore magna aliqua.</p><div class="stars">★★★★★</div></div>
<div class="t-card" style="left:449px"><div class="avatar" style="background:linear-gradient(180deg,#d8c9a6,#a89878)" role="img" aria-label="Portrait of a smiling woman"></div><span class="quote">“</span><h3>Jordan Reyes</h3><p>Lorem ipsum dolor sit amet, consectetur adipiscing elit, sed do eiusmod tempor incididunt ut labore et dolore magna aliqua.</p><div class="stars">★★★★★</div></div>
<div class="t-card" style="left:784px"><div class="avatar" style="background:linear-gradient(180deg,#dcdce0,#9b2430 70%)" role="img" aria-label="Portrait of a man in a red shirt"></div><span class="quote">“</span><h3>Jordan Reyes</h3><p>Lorem ipsum dolor sit amet, consectetur adipiscing elit, sed do eiusmod tempor incididunt ut labore et dolore magna aliqua.</p><div class="stars">★★★★★</div></div>
<div class="arrow" style="left:24px;top:4218px;border-color:#777"><svg width="36" height="36" viewBox="0 0 36 36"><polyline points="21,11 14,18 21,25" fill="none" stroke="#777" stroke-width="2"/></svg></div>
<div class="arrow" style="left:1123px;top:4218px;border-color:#1ed8b7"><svg width="36" height="36" viewBox="0 0 36 36"><polyline points="15,11 22,18 15,25" fill="none" stroke="#1ed8b7" stroke-width="2"/></svg></div>

<footer class="footer">
  <svg class="abs" style="left:0;top:-4px" width="1200" height="100" viewBox="0 0 1200 100">
    <polygon points="0,0 1200,0 1200,8 290,82 0,4" fill="#fff"/>
    <polygon points="0,4 290,82 1200,8 1200,18 290,92 0,14" fill="var(--blue)"/>
  </svg>
  <div class="abs" style="left:112px;top:220px;display:flex;align-items:center;gap:10px"><span class="brand-name" style="color:#fff">The Clear Quill</span><span class="brand-dot" style="background:#fff"></span></div>
  <h4 style="left:388px">VISIT US</h4>
  <svg class="abs" style="left:388px;top:230px" width="14" height="18" viewBox="0 0 14 18"><path d="M7 0 a7 7 0 0 1 7 7 c0 5 -7 11 -7 11 s-7 -6 -7 -11 a7 7 0 0 1 7 -7z" fill="#2fe6c8"/><circle cx="7" cy="7" r="2.5" fill="var(--navy)"/></svg>
  <div class="item" style="left:420px;top:226px;width:210px">TheClearQuill<br>Lorem ipsum dolor sit amet, consectetur</div>
  <h4 style="left:681px">CONTACT US</h4>
  <svg class="abs" style="left:681px;top:232px" width="15" height="15" viewBox="0 0 12 12"><path d="M2 0 l3 3 -1.5 2 q1.5 3 3.5 3.5 l2 -1.5 3 3 -2 2 q-7 0 -10 -10z" fill="#2fe6c8"/></svg>
  <div class="item" style="left:715px;top:226px">(555) 014-2270</div>
  <svg class="abs" style="left:681px;top:270px" width="15" height="12" viewBox="0 0 14 11"><rect width="14" height="11" fill="#2fe6c8"/><polyline points="0,0 7,6 14,0" fill="none" stroke="#070d2b" stroke-width="1.2"/></svg>
  <div class="item" style="left:715px;top:263px">info@TheClearQuill.com</div>
  <div class="abs" style="left:388px;top:319px;width:583px;height:1px;background:#5a5f7a"></div>
  <div class="item" style="left:388px;top:349px;font-size:15px">2023 TheClearQuill. All Rights Reserved.</div>
  <h4 style="left:982px">QUICK LINKS</h4>
  <div class="abs links" style="left:982px;top:225px"><a>Home</a><a>Work with Us</a><a>Work for Us</a><a>About Us</a><a>Contact</a></div>
</footer>

</body>
</html>
```